I need a Label design for my tavin 58 kombucha brand that is launching soon

I want a label to go on my tavin 58 kombucha bottle.
I have a logo image uploaded in the files but I am open to changes to this logo or even a completely New one if you think you can do better. This logo is based on the idea of an s-shaped naga. I particularly like the nagas from temples in luang prabang.
I also want to include the slogan - dare to be delicious.
The label should be some kind of oval at 80mm high by 70mm wide.
The label will go on a clear glass bottle. The kombucha will be visible and comes in different shades of red,yellow and purple.
The word kombucha should be clearly visible.
i want a very colorful, playful label. I'm very keen to see your ideas and I want something original.
Fermented foods and beverages

```html
<!DOCTYPE html>
<html lang="en">
<head>
<meta charset="utf-8">
<title>tavin 58 kombucha label</title>
<link rel="stylesheet" href="https://fonts.googleapis.com/css2?family=Kaushan+Script&family=Tinos&display=swap">
<style>
  :root {
    --page: #ffffff;
    --label-orange: #f6ab3c;
    --label-orange-light: #f9bd55;
    --label-orange-deep: #f19a2c;
    --comb-tone: #f4a32f;
    --comb-tone-deep: #ee9426;
    --leaf-light: #8fd14f;
    --leaf-mid: #4fae3a;
    --leaf-deep: #2e8a2e;
    --title-green: #1d6b3a;
    --slogan-white: #fffaf0;
    --mark-white: #ffffff;
  }
  html, body {
    margin: 0;
    padding: 0;
    width: 1200px;
    height: 1200px;
    overflow: hidden;
    background: var(--page);
  }
  .label-canvas {
    display: block;
    width: 1200px;
    height: 1200px;
  }
  .brand-name {
    font-family: "Tinos", serif;
    font-size: 34px;
    fill: var(--mark-white);
  }
  .product-title {
    font-family: "Kaushan Script", cursive;
    font-size: 168px;
    fill: var(--title-green);
  }
  .slogan {
    font-family: "Tinos", serif;
    font-size: 40px;
    letter-spacing: 1px;
    fill: var(--slogan-white);
  }
</style>
</head>
<body>
<svg class="label-canvas" viewBox="0 0 1200 1200" xmlns="http://www.w3.org/2000/svg">
  <defs>
    <clipPath id="label-shape">
      <ellipse cx="600" cy="600" rx="420" ry="480"/>
    </clipPath>
    <linearGradient id="label-fill" x1="0" y1="0" x2="0" y2="1">
      <stop offset="0" stop-color="var(--label-orange-light)"/>
      <stop offset="0.5" stop-color="var(--label-orange)"/>
      <stop offset="1" stop-color="var(--label-orange-deep)"/>
    </linearGradient>
    <radialGradient id="comb-fill" cx="0.5" cy="0.5" r="0.5">
      <stop offset="0" stop-color="var(--comb-tone-deep)" stop-opacity="0.9"/>
      <stop offset="1" stop-color="var(--comb-tone)" stop-opacity="0"/>
    </radialGradient>
    <linearGradient id="leaf-fill" x1="0" y1="0" x2="1" y2="1">
      <stop offset="0" stop-color="var(--leaf-light)"/>
      <stop offset="0.5" stop-color="var(--leaf-mid)"/>
      <stop offset="1" stop-color="var(--leaf-deep)"/>
    </linearGradient>
  </defs>

  <g class="label" clip-path="url(#label-shape)">
    <rect class="label-ground" x="180" y="120" width="840" height="960" fill="url(#label-fill)"/>

    <ellipse class="honeycomb-pattern" role="img" aria-label="Soft honeycomb pattern in deeper orange"
             cx="620" cy="880" rx="360" ry="220" fill="url(#comb-fill)"/>

    <path class="leaves-upper" role="img" aria-label="Swirl of fresh green tea leaves drifting across the label"
          d="M190 520 C300 440 420 330 560 360 C690 390 780 430 880 330 C930 280 980 250 1020 240 L1020 300 C960 330 920 400 860 440 C760 500 650 450 560 430 C430 400 320 480 190 580 Z"
          fill="url(#leaf-fill)" opacity="0.55"/>

    <path class="leaves-lower" role="img" aria-label="Scattered green tea leaves along the lower edge"
          d="M270 930 C360 860 440 820 540 850 C640 880 700 920 800 880 C880 850 940 800 990 760 L1000 840 C940 900 880 950 800 960 C700 975 620 930 540 920 C440 910 360 950 290 990 Z"
          fill="url(#leaf-fill)" opacity="0.55"/>
  </g>

  <g class="brand-mark">
    <circle class="brand-dot" cx="600" cy="178" r="22" fill="var(--mark-white)"/>
    <text class="brand-name" x="600" y="240" text-anchor="middle">tavin 58</text>
  </g>

  <text class="product-title" x="606" y="640" text-anchor="middle" transform="rotate(-3 606 600)">kombucha</text>

  <text class="slogan" x="600" y="692" text-anchor="middle">DARE TO BE DELICIOUS</text>
</svg>
</body>
</html>
```